Harbor Kindness Fund - New Website Design

I need a site that looks like this http://wheelgift-relief.org for boat donations. So please replace the cars with boats.

```html
<!DOCTYPE html>
<html lang="en">
<head>
<meta charset="utf-8">
<title>Harbor Kindness Fund</title>
<link href="https://fonts.googleapis.com/css2?family=Open+Sans:ital,wght@0,400;0,600;0,700;1,400&display=swap" rel="stylesheet">
<style>
:root{
  --pink:#e5177e;
  --blue:#1fa9da;
  --cyan:#2bb8e2;
  --yellow:#f1e11c;
  --ink:#1d1d1d;
  --grey:#9a9a9a;
  --soft:#f1f1f1;
  --band:#1b9dcf;
  --footer:#333333;
  --white:#ffffff;
}
*{margin:0;padding:0;box-sizing:border-box}
html,body{width:1200px;height:3516px;overflow:hidden}
body{font-family:"Open Sans",Arial,sans-serif;color:var(--ink);background:var(--white);position:relative}
.abs{position:absolute}
/* header */
.site-header{position:absolute;left:0;top:0;width:1200px;height:112px;background:var(--white)}
.brand{position:absolute;left:59px;top:36px;width:220px;display:flex;align-items:center;gap:10px}
.brand-mark{width:34px;height:34px;border-radius:50%;background:var(--pink);flex:none}
.brand-name{font-size:16px;font-weight:700;color:var(--ink);white-space:nowrap}
.main-nav a{position:absolute;top:48px;font-size:19px;font-weight:600;color:var(--ink);text-decoration:none;white-space:nowrap}
.nav-active{position:absolute;left:300px;top:103px;width:60px;height:9px;background:var(--blue)}
.btn{display:flex;align-items:center;justify-content:center;color:var(--white);font-weight:600;text-transform:uppercase;text-decoration:none}
.header-donate{position:absolute;left:944px;top:33px;width:204px;height:54px;background:var(--pink);font-size:18px}
/* hero */
.hero-photo{position:absolute;left:0;top:112px;width:1200px;height:568px;
  background:radial-gradient(ellipse 260px 280px at 360px 330px,#f0d6c8 0%,#e7b9b0 40%,transparent 70%),
  radial-gradient(ellipse 300px 200px at 360px 180px,#e0417f 0%,transparent 75%),
  linear-gradient(90deg,#4e6e2c 0%,#7d9a45 35%,#9bb35a 60%,#5d7a34 100%)}
.donation-form{position:absolute;left:722px;top:159px;width:424px;height:474px;background:rgba(38,134,165,.86)}
.donation-form h2{position:absolute;left:0;top:28px;width:100%;text-align:center;color:var(--white);font-size:35px;font-weight:700;line-height:42px}
.field{position:absolute;left:35px;width:361px;height:47px;border:1px solid rgba(255,255,255,.8);color:#e8f3f7;font-style:italic;font-size:17px;padding:0 16px;display:flex;align-items:center;justify-content:space-between}
.form-continue{position:absolute;left:94px;top:389px;width:234px;height:62px;background:var(--pink);font-size:25px}
/* section heads */
.section-title{position:absolute;left:0;width:1200px;text-align:center;font-size:37px;font-weight:600;text-transform:uppercase;color:var(--ink)}
.section-title span{color:var(--pink)}
.section-lead{position:absolute;left:140px;width:920px;text-align:center;font-size:16px;color:var(--grey);line-height:21px}
/* steps */
.step-num{position:absolute;top:860px;width:131px;height:131px;border-radius:50%;display:flex;align-items:center;justify-content:center;color:var(--white);font-size:84px;font-weight:700;font-style:italic}
.step-label{position:absolute;top:872px;font-size:26px;font-weight:700;white-space:nowrap}
.step-text{position:absolute;top:910px;width:210px;font-size:16px;color:#b3b3b3;line-height:19px}
/* gallery */
.gallery-bg{position:absolute;left:0;top:1038px;width:1200px;height:685px;background:var(--soft)}
.tile{position:absolute;width:365px;height:215px}
/* services */
.rule{position:absolute;top:1976px;height:1px;background:#d9d9d9}
.service-icon{position:absolute;top:1918px;width:110px;height:100px}
.service-title{position:absolute;top:2028px;width:340px;text-align:center;font-size:21px;font-weight:600}
.service-text{position:absolute;top:2070px;width:290px;text-align:center;font-size:14px;color:var(--grey);line-height:19px}
.service-more{position:absolute;top:2138px;width:340px;text-align:center;font-size:13px;font-weight:700}
.services-more{position:absolute;left:511px;top:2206px;width:185px;height:54px;background:var(--cyan);font-size:16px;font-weight:700}
/* faq */
.faq-band{position:absolute;left:0;top:2320px;width:1200px;height:258px;background:linear-gradient(180deg,#27a9dc 0%,#1a93c4 55%,#1d9fcf 100%)}
.faq-title{position:absolute;left:0;top:36px;width:1200px;text-align:center;color:var(--white);font-size:54px;font-weight:700}
.faq-btn{position:absolute;left:401px;top:127px;width:403px;height:82px;background:var(--pink);font-size:29px;font-weight:700}
/* blog */
.blog-card{position:absolute;top:2698px;height:281px;background:var(--blue);color:var(--white)}
.blog-photo{position:absolute;left:0;top:0;width:271px;height:281px}
.blog-body{position:absolute;left:288px;top:14px;right:12px}
.blog-date{font-size:14px;color:var(--pink);font-weight:600;display:flex;align-items:center;gap:8px}
.blog-heading{font-size:25px;font-weight:700;line-height:32px;margin-top:6px}
.blog-text{font-size:15px;line-height:19px;margin-top:8px}
.blog-comments{font-size:15px;font-weight:600;margin-top:14px;display:flex;align-items:center;gap:10px}
/* footer */
.site-footer{position:absolute;left:0;top:3066px;width:1200px;height:450px;background:var(--footer);color:var(--white)}
.footer-brand{position:absolute;left:452px;top:47px;width:298px;height:117px;border-radius:50%;background:var(--white);display:flex;align-items:center;justify-content:center;gap:10px}
.footer-text{position:absolute;left:160px;top:182px;width:880px;text-align:center;font-size:15px;font-weight:600;line-height:19px}
.footer-rule{position:absolute;left:163px;top:267px;width:875px;height:1px;background:#8a8a8a}
.social{position:absolute;top:300px;width:66px;height:66px;border-radius:50%}
.copyright{position:absolute;left:0;top:388px;width:1200px;text-align:center;font-size:15px}
.footer-strip{position:absolute;left:0;bottom:0;width:1200px;height:14px;background:var(--blue)}
</style>
</head>
<body>

<header class="site-header">
  <div class="brand"><span class="brand-mark"></span><span class="brand-name">Harbor Kindness Fund</span></div>
  <nav class="main-nav">
    <a href="#" style="left:300px">HOME</a>
    <a href="#" style="left:394px">ABOUT US</a>
    <a href="#" style="left:516px">QUESTIONS</a>
    <a href="#" style="left:651px">GET STARTED</a>
    <a href="#" style="left:796px">CONTACT US</a>
  </nav>
  <span class="nav-active"></span>
  <a href="#" class="btn header-donate">Donate Now</a>
</header>

<section>
  <div class="hero-photo" role="img" aria-label="Young child wearing a pink headscarf outdoors"></div>
  <form class="donation-form">
    <h2>FILL THE DONATION<br>FORM</h2>
    <div class="field" style="top:128px">enter your name
      <svg width="14" height="16" viewBox="0 0 14 16"><circle cx="7" cy="4" r="4" fill="#fff"/><path d="M0 16c0-5 3-7 7-7s7 2 7 7z" fill="#fff"/></svg></div>
    <div class="field" style="top:192px">enter your phone number
      <svg width="15" height="15" viewBox="0 0 15 15"><path d="M3 1l3 3-2 2c1 2 3 4 5 5l2-2 3 3-2 3C6 15 0 9 1 3z" fill="#fff"/></svg></div>
    <div class="field" style="top:255px">enter your e-mail address
      <svg width="17" height="12" viewBox="0 0 17 12"><rect width="17" height="12" fill="#fff"/><path d="M0 0l8.5 7L17 0" stroke="#2686a5" stroke-width="1.5" fill="none"/></svg></div>
    <div class="field" style="top:318px">enter your zip-code
      <svg width="12" height="8" viewBox="0 0 12 8"><path d="M0 0h12L6 8z" fill="#fff"/></svg></div>
    <a href="#" class="btn form-continue">Continue</a>
  </form>
</section>

<section>
  <h2 class="section-title" style="top:720px">Welcome to <span>our website !</span></h2>
  <p class="section-lead" style="top:779px">Aenean imperdiet neque lectus, non volutpat erat interdum pulvinar. Suspendisse maximus sed augue ac finibus.</p>

  <div class="step-num" style="left:59px;background:var(--pink)">1</div>
  <div class="step-label" style="left:211px;color:var(--pink)">Donate Now</div>
  <p class="step-text" style="left:211px">Aenean imperdiet neque lectus, non volutpat</p>

  <div class="step-num" style="left:424px;background:var(--cyan)">2</div>
  <div class="step-label" style="left:574px;color:var(--cyan)">Hands On Help</div>
  <p class="step-text" style="left:574px">Aenean imperdiet neque lectus, non volutpat</p>

  <div class="step-num" style="left:799px;background:var(--yellow)">3</div>
  <div class="step-label" style="left:945px;color:var(--yellow)">Our Program</div>
  <p class="step-text" style="left:945px">Aenean imperdiet neque lectus, non volutpat</p>
</section>

<section>
  <div class="gallery-bg"></div>
  <h2 class="section-title" style="top:1083px">Together we can <span>make difference</span></h2>
  <p class="section-lead" style="top:1133px">Aliquam nunc lorem, lacinia vel elementum ut, vulputate eu diam. Phasellus erat turpis, sagittis id neque vel, semper congue ex.</p>
  <div class="tile" style="left:59px;top:1219px;background:linear-gradient(135deg,#57b9dd,#3aa6d2)" role="img" aria-label="Volunteers with a young patient, highlighted">
    <svg class="abs" style="left:165px;top:90px" width="36" height="36" viewBox="0 0 36 36"><circle cx="15" cy="15" r="11" fill="none" stroke="#fff" stroke-width="3"/><path d="M23 23l10 10M10 15h10M15 10v10" stroke="#fff" stroke-width="3"/></svg>
  </div>
  <div class="tile" style="left:424px;top:1219px;background:linear-gradient(135deg,#c79a6f,#8f6d54 60%,#d4a33c)" role="img" aria-label="Man and child patient sharing a moment"></div>
  <div class="tile" style="left:781px;top:1219px;width:365px;background:linear-gradient(135deg,#a37e5c,#5c4534 60%,#d9a05a)" role="img" aria-label="Child in a mask with a caregiver"></div>
  <div class="tile" style="left:59px;top:1434px;height:214px;background:linear-gradient(135deg,#6f6a60,#c9b49a 50%,#3f3b36)" role="img" aria-label="Group of volunteers and children"></div>
  <div class="tile" style="left:424px;top:1434px;height:214px;background:linear-gradient(135deg,#2f2a2a,#b48e74 50%,#3c4a6a)" role="img" aria-label="Family group smiling together"></div>
  <div class="tile" style="left:781px;top:1434px;height:214px;background:linear-gradient(135deg,#33383e,#c49a84 50%,#e58fb4)" role="img" aria-label="Man with a smiling young girl"></div>
</section>

<section>
  <h2 class="section-title" style="top:1762px">Donate boat <span>to charity</span></h2>
  <p class="section-lead" style="top:1811px">Aliquam nunc lorem, lacinia vel elementum ut, vulputate eu diam. Phasellus erat turpis, sagittis id neque vel, loren ipsum semper congue ex.</p>

  <span class="rule" style="left:59px;width:150px"></span>
  <span class="rule" style="left:322px;width:225px"></span>
  <span class="rule" style="left:660px;width:210px"></span>
  <span class="rule" style="left:990px;width:156px"></span>

  <svg class="service-icon" style="left:210px" viewBox="0 0 110 100" fill="none" stroke="var(--pink)" stroke-width="3">
    <path d="M15 62h80l-10 18H25z"/><rect x="32" y="44" width="46" height="18"/><rect x="44" y="28" width="22" height="16"/><path d="M55 28V14M10 90c8-5 14 5 22 0s14 5 22 0 14 5 22 0 14 5 22 0"/>
  </svg>
  <div class="service-title" style="left:95px;color:var(--pink)">We Accept All Baots</div>
  <p class="service-text" style="left:120px">It is a long established fact that a reader will be distracted by the readable content of a page when</p>
  <div class="service-more" style="left:95px;color:var(--pink)">READ MORE</div>

  <svg class="service-icon" style="left:547px" viewBox="0 0 110 100" fill="none" stroke="var(--cyan)" stroke-width="3">
    <circle cx="62" cy="26" r="18"/><path d="M62 16v20M56 21h9a4 4 0 010 8h-6a4 4 0 000 8h9"/><path d="M12 60h14v30H12zM26 64c14-6 24-4 32 2h14a5 5 0 010 10H52M26 86l26 4 40-20a6 6 0 00-6-9L70 68"/>
  </svg>
  <div class="service-title" style="left:432px;color:var(--cyan)">Hassale Free Donation</div>
  <p class="service-text" style="left:457px">It is a long established fact that a reader will be distracted by the readable content of a page when</p>
  <div class="service-more" style="left:432px;color:var(--cyan)">READ MORE</div>

  <svg class="service-icon" style="left:878px" viewBox="0 0 110 100" fill="none" stroke="var(--yellow)" stroke-width="3">
    <circle cx="55" cy="24" r="17"/><path d="M55 14v20M50 19h8a4 4 0 010 8h-6a4 4 0 000 8h8"/><path d="M18 52l6 30 14 14M92 52l-6 30-14 14M28 62l14 14 4 14M82 62L68 76l-4 14"/>
  </svg>
  <div class="service-title" style="left:763px;color:var(--yellow)">Help Fund Program</div>
  <p class="service-text" style="left:788px">It is a long established fact that a reader will be distracted by the readable content of a page when</p>
  <div class="service-more" style="left:763px;color:var(--yellow)">READ MORE</div>

  <a href="#" class="btn services-more">Read More</a>
</section>

<section class="faq-band" role="img" aria-label="Blue-toned photo of a boat on the water">
  <h2 class="faq-title">Frequently Ask Questions</h2>
  <a href="#" class="btn faq-btn">View Questions</a>
</section>

<section>
  <h2 class="section-title" style="top:2612px">Our blog <span>post</span></h2>

  <article class="blog-card" style="left:59px;width:527px">
    <div class="blog-photo" style="background:linear-gradient(135deg,#3b6fa8,#d7b89a 50%,#6fb256)" role="img" aria-label="Children holding a sign that reads Give"></div>
    <div class="blog-body">
      <div class="blog-date"><svg width="14" height="14" viewBox="0 0 14 14"><rect y="2" width="14" height="12" fill="var(--pink)"/><rect x="2" y="6" width="10" height="6" fill="#1fa9da"/></svg>20 JUL 2017</div>
      <h3 class="blog-heading">Loren Ipsum Dolar Amet</h3>
      <p class="blog-text">But in certain circumstances and owing to the claims of duty or But in certain circumstances and owing to the claims sures</p>
      <div class="blog-comments"><svg width="18" height="14" viewBox="0 0 18 14"><ellipse cx="7" cy="6" rx="7" ry="5" fill="#fff"/><path d="M2 9l-1 5 5-3z" fill="#fff"/></svg>2 Comments</div>
    </div>
  </article>

  <article class="blog-card" style="left:638px;width:506px">
    <div class="blog-photo" style="width:260px;background:linear-gradient(135deg,#5a3c2c,#c99a7a 50%,#d04d3b)" role="img" aria-label="Young patient with a friend smiling"></div>
    <div class="blog-body" style="left:275px">
      <div class="blog-date"><svg width="14" height="14" viewBox="0 0 14 14"><rect y="2" width="14" height="12" fill="var(--pink)"/><rect x="2" y="6" width="10" height="6" fill="#1fa9da"/></svg>26 JUL 2017</div>
      <h3 class="blog-heading">Loren Ipsum Dolar Amet</h3>
      <p class="blog-text">But in certain circumstances and owing to the claims of duty But in certain circumstances and owing to occur that</p>
      <div class="blog-comments"><svg width="18" height="14" viewBox="0 0 18 14"><ellipse cx="7" cy="6" rx="7" ry="5" fill="#fff"/><path d="M2 9l-1 5 5-3z" fill="#fff"/></svg>4 Comments</div>
    </div>
  </article>
</section>

<footer class="site-footer">
  <div class="footer-brand"><span class="brand-mark" style="width:30px;height:30px"></span><span class="brand-name" style="font-size:19px">Harbor Kindness Fund</span></div>
  <p class="footer-text">At vero eos et accusamus et iusto odio dignissimos ducimus qui blanditiis praesentium voluptatum deleniti atque corrupti quos dolores et quas molestias excepturi sint occaecati cupiditate non provident, similique sunt in culpa qui officia deserunt mollitia animi</p>
  <span class="footer-rule"></span>
  <a href="#" class="social" style="left:427px;background:#3b5ca8" aria-label="Social link one"></a>
  <a href="#" class="social" style="left:499px;background:#1ea0dc" aria-label="Social link two"></a>
  <a href="#" class="social" style="left:567px;background:#e25a2a" aria-label="Social link three"></a>
  <a href="#" class="social" style="left:636px;background:#1f78b4" aria-label="Social link four"></a>
  <a href="#" class="social" style="left:711px;background:#c3222a" aria-label="Social link five"></a>
  <p class="copyright">Copyright2017.All Right Reserved</p>
  <span class="footer-strip"></span>
</footer>

</body>
</html>
```